Quorvane Exploration and Production

We need a powerpoint design for a new exploration company. I would like to either use black logo or change color to a cardinal color. We explore oil and gas exploration. We would like to see designs with a cardinal color. The ppt would be a universal ppt used for presenting deals.

```html
<!DOCTYPE html>
<html lang="en">
<head>
<meta charset="utf-8">
<title>Quorvane Exploration and Production – Deal Presentation</title>
<link rel="stylesheet" href="https://fonts.googleapis.com/css2?family=Archivo:wght@300;400;600;700;900&display=swap">
<style>
:root{
  --stage:#78829a;
  --paper:#ffffff;
  --ink:#1a1a1a;
  --ink-soft:#444444;
  --grey-dark:#3a3a3a;
  --grey-mid:#5c5c5c;
  --grey-light:#9a9a9a;
  --grey-pale:#e7e7e8;
  --label:#6b6b6b;
}
*{box-sizing:border-box;margin:0;padding:0}
html,body{width:1200px;height:1200px;overflow:hidden}
body{background:var(--stage);font-family:"Archivo",Arial,sans-serif;color:var(--ink);position:relative}
.slide{position:absolute;width:469px;height:263px;background:var(--paper);overflow:hidden;box-shadow:0 2px 4px rgba(0,0,0,.35)}
.s1{left:98px;top:105px}.s2{left:633px;top:105px}
.s3{left:98px;top:449px}.s4{left:633px;top:449px}
.s5{left:98px;top:793px}.s6{left:633px;top:793px}
.deco{position:absolute;inset:0;width:100%;height:100%}
.photo{position:absolute}
.rule{position:absolute;height:1px;background:var(--ink)}
.footer-text{position:absolute;font-size:5.5px;color:var(--ink)}
.footer-mark{position:absolute;width:17px;height:17px;border-radius:50%;background:var(--ink)}
.heading{position:absolute;font-weight:600;color:var(--ink-soft);font-size:12.5px;line-height:1.3}
.body{position:absolute;font-size:5.3px;line-height:1.45;color:var(--ink-soft)}
.body.bold{font-weight:600}
/* cover */
.cover-rule{position:absolute;height:1.5px;background:var(--ink)}
.cover-kicker{position:absolute;left:28px;top:146px;font-size:17px;font-weight:300;color:var(--ink-soft)}
.cover-title{position:absolute;left:28px;top:166px;font-size:32px;font-weight:900;letter-spacing:.5px;color:var(--ink);white-space:nowrap;z-index:2}
.cover-sub{position:absolute;left:28px;top:218px;font-size:9.5px;color:var(--ink-soft)}
.cover-badge{position:absolute;left:280px;top:37px;width:112px;height:112px;border-radius:50%;background:#0d0d0d;display:flex;align-items:center;justify-content:center;z-index:2}
.cover-badge span{color:#fff;font-weight:700;font-size:14px;letter-spacing:1px}
/* map */
.map-label{position:absolute;font-size:3.6px;line-height:1.35;color:var(--ink-soft)}
.map-label b{display:block;background:var(--label);color:#fff;font-weight:400;padding:0 2px}
/* bars */
.bar{position:absolute;left:34px;width:136px;height:19px;color:#fff;font-size:5.5px;padding:7px 8px}
.bullet{position:absolute;left:34px;width:200px;font-size:5.3px;line-height:1.45;font-weight:600;color:var(--ink-soft);padding-left:10px}
.bullet::before{content:"";position:absolute;left:0;top:2px;width:4px;height:4px;background:var(--ink-soft)}
</style>
</head>
<body>

<!-- Cover -->
<section class="slide s1">
  <div class="photo" role="img" aria-label="Photo of a drilling rig and pipe racks under a blue sky" style="left:165px;top:0;width:304px;height:263px;background:linear-gradient(180deg,#3a6fc0 0%,#5a88cc 45%,#8a8f98 62%,#6b5a4e 82%,#9a5a3a 100%)"></div>
  <svg class="deco" viewBox="0 0 469 263" aria-hidden="true">
    <path d="M300 0 A105 105 0 0 0 405 115 A105 105 0 0 0 469 140 L469 160 A125 125 0 0 1 340 0 Z" fill="#5a6170" opacity=".8"/>
  </svg>
  <div class="cover-rule" style="left:26px;top:26px;width:122px"></div>
  <div class="cover-kicker">LOREM IPSUM</div>
  <div class="cover-title">LOREM IPSUM</div>
  <div class="cover-rule" style="left:26px;top:208px;width:122px"></div>
  <div class="cover-sub">LOREM IPSUM</div>
  <div class="cover-badge"><span>QUORVANE</span></div>
</section>

<!-- Global presence -->
<section class="slide s2">
  <svg class="deco" viewBox="0 0 469 263" aria-hidden="true">
    <circle cx="10" cy="70" r="60" fill="none" stroke="var(--grey-pale)" stroke-width="22"/>
  </svg>
  <div class="heading" style="left:26px;top:14px;font-size:12px">Lorem ipsum dolor sit amet.</div>
  <div class="photo" role="img" aria-label="World map with operating locations marked" style="left:70px;top:66px;width:336px;height:160px;border-radius:40px 60px 30px 50px;background:linear-gradient(90deg,#6a6a6a 0%,#8a8a8a 30%,#c8c8c8 45%,#bdbdbd 70%,#cfcfcf 100%)"></div>
  <div class="map-label" style="left:26px;top:52px"><b>Lorem Ipsum</b>Lorem Ipsum</div>
  <div class="map-label" style="left:26px;top:68px"><b>Lorem Ipsum</b>Lorem Ipsum<br>Lorem Ipsum<br>Lorem Ipsum</div>
  <div class="map-label" style="left:26px;top:146px"><b>Lorem Ipsum</b>Lorem Ipsum</div>
  <div class="map-label" style="left:26px;top:190px"><b>Lorem Ipsum</b>Lorem Ipsum</div>
  <div class="map-label" style="left:188px;top:48px"><b>Lorem Ipsum</b>Lorem Ipsum<br>Lorem Ipsum</div>
  <div class="map-label" style="left:234px;top:48px"><b>Lorem Ipsum</b>Lorem Ipsum<br>Lorem Ipsum</div>
  <div class="map-label" style="left:278px;top:48px"><b>Lorem Ipsum</b>Lorem Ipsum</div>
  <div class="map-label" style="left:318px;top:48px"><b>Lorem Ipsum</b>Lorem Ipsum</div>
  <div class="map-label" style="left:357px;top:48px"><b>Lorem Ipsum</b>Lorem Ipsum</div>
  <div class="map-label" style="left:178px;top:105px"><b>Lorem Ipsum</b>Lorem Ipsum</div>
  <div class="map-label" style="left:178px;top:122px"><b>Lorem Ipsum</b>Lorem Ipsum</div>
  <div class="map-label" style="left:178px;top:138px"><b>Lorem Ipsum</b>Lorem Ipsum</div>
  <div class="map-label" style="left:170px;top:153px"><b>Lorem Ipsum</b>Lorem Ipsum</div>
  <div class="map-label" style="left:197px;top:172px"><b>Lorem Ipsum</b>Lorem Ipsum</div>
  <div class="map-label" style="left:197px;top:188px"><b>Lorem Ipsum</b>Lorem Ipsum</div>
  <div class="map-label" style="left:197px;top:204px"><b>Lorem Ipsum</b>Lorem Ipsum<br>Lorem Ipsum<br>Lorem Ipsum<br>Lorem Ipsum</div>
  <div class="map-label" style="left:275px;top:172px"><b>Lorem Ipsum</b>Lorem Ipsum<br>Lorem Ipsum</div>
  <div class="map-label" style="left:275px;top:194px"><b>Lorem Ipsum</b>Lorem Ipsum</div>
  <div class="map-label" style="left:411px;top:68px"><b>Lorem Ipsum</b>Lorem Ipsum<br>Lorem Ipsum<br>Lorem Ipsum</div>
  <div class="map-label" style="left:411px;top:130px"><b>Lorem Ipsum</b>Lorem Ipsum</div>
  <div class="map-label" style="left:411px;top:145px"><b>Lorem Ipsum</b>Lorem Ipsum</div>
  <div class="map-label" style="left:411px;top:160px"><b>Lorem Ipsum</b>Lorem Ipsum</div>
  <div class="map-label" style="left:411px;top:175px"><b>Lorem Ipsum</b>Lorem Ipsum</div>
  <div class="map-label" style="left:411px;top:189px"><b>Lorem Ipsum</b>Lorem Ipsum</div>
  <svg class="deco" viewBox="0 0 469 263" aria-hidden="true" stroke="#555" stroke-width=".4" fill="none">
    <path d="M58 56 L110 80 L126 118"/><path d="M58 146 L92 146"/><path d="M58 194 L150 194 L170 160"/>
    <path d="M210 55 L222 115"/><path d="M258 55 L230 120"/><path d="M300 55 L236 124"/>
    <path d="M410 72 L340 140"/><path d="M410 134 L352 150"/><path d="M410 164 L345 168"/>
    <g fill="#111" stroke="none"><circle cx="126" cy="118" r="1.5"/><circle cx="222" cy="115" r="1.5"/><circle cx="230" cy="120" r="1.5"/><circle cx="236" cy="124" r="1.5"/><circle cx="340" cy="140" r="1.5"/><circle cx="352" cy="150" r="1.5"/><circle cx="345" cy="168" r="1.5"/><circle cx="170" cy="160" r="1.5"/></g>
  </svg>
  <div class="rule" style="left:13px;top:245px;width:428px"></div>
  <div class="footer-text" style="left:378px;top:250px">Lorem ipsum | 04</div>
  <div class="footer-mark" style="left:438px;top:237px"></div>
</section>

<!-- Overview -->
<section class="slide s3">
  <svg class="deco" viewBox="0 0 469 263" aria-hidden="true">
    <circle cx="400" cy="70" r="80" fill="none" stroke="var(--grey-pale)" stroke-width="30"/>
  </svg>
  <div class="photo" role="img" aria-label="Photo of drilling rigs on a desert plain under a blue sky" style="left:0;top:0;width:205px;height:263px;background:linear-gradient(180deg,#2f63b5 0%,#6d99d6 55%,#8d7e5c 62%,#a08664 80%,#b88f6c 100%)"></div>
  <div class="body" style="left:231px;top:77px;width:200px">Lorem ipsum dolor sit amet, consectetur adipiscing elit. Fusce ut diam magna. Cras at orci egestas, tincidunt tortor vitae, viverra mi. Vestibulum in ipsum sapien.</div>
  <div class="heading" style="left:231px;top:107px">Lorem ipsum dolor sit amet.</div>
  <div class="body" style="left:231px;top:125px;width:200px">Lorem ipsum dolor sit amet, consectetur adipiscing elit. Fusce ut diam magna. Cras at orci egestas, tincidunt tortor vitae, viverra mi. Vestibulum in ipsum sapien. Fusce in ipsum id augue ultricies consectetur. Sed et convallis lacus. Nam pretium est eu enim sagittis, quis placerat eros faucibus. Nullam gravida lorem libero, vel sagittis felis interdum non. Duis sit amet commodo libero. Nunc vestibulum facilisis magna sit amet iaculis. Sed viverra, augue sit amet imperdiet lacinia, est sapien sollicitudin neque, ut pellentesque ante sapien vitae nunc. In hac habitasse platea dictumst. Cras porttitor et eros sed dictum.</div>
  <div class="rule" style="left:212px;top:245px;width:229px"></div>
  <div class="footer-text" style="left:378px;top:250px">Lorem ipsum | 02</div>
  <div class="footer-mark" style="left:438px;top:237px"></div>
</section>

<!-- Process wheel -->
<section class="slide s4">
  <svg class="deco" viewBox="0 0 469 263" aria-hidden="true">
    <circle cx="30" cy="20" r="50" fill="none" stroke="var(--grey-pale)" stroke-width="24"/>
    <circle cx="330" cy="180" r="110" fill="none" stroke="var(--grey-pale)" stroke-width="26"/>
  </svg>
  <div class="heading" style="left:32px;top:78px">Lorem ipsum dolor sit amet,<br>consectetur adipiscing elit.</div>
  <div class="body bold" style="left:32px;top:120px;width:192px">Lorem ipsum dolor sit amet, consectetur adipiscing elit. Fusce ut diam magna. Cras at orci egestas, tincidunt tortor vitae, viverra mi. Vestibulum in ipsum sapien. Fusce in ipsum id augue ultricies consectetur. Sed et convallis lacus. Nam pretium est eu enim sagittis, quis placerat eros faucibus. Nullam gravida lorem libero, vel sagittis felis interdum non. Duis sit amet commodo libero. Nunc vestibulum facilisis magna sit amet iaculis. Sed viverra, augue sit amet imperdiet lacinia, est sapien sollicitudin neque, ut pellentesque ante sapien vitae nunc. In hac habitasse platea dictumst. Cras porttitor et eros sed dictum.</div>
  <svg class="deco" viewBox="0 0 469 263" font-family="Archivo, Arial, sans-serif">
    <defs>
      <path id="ring-top" d="M247.1 149.6 A91 91 0 1 1 422.9 149.6"/>
      <path id="ring-bottom" d="M250.4 169.1 A95 95 0 0 0 419.6 169.1"/>
    </defs>
    <circle cx="335" cy="126" r="102" fill="#333"/>
    <g stroke="#fff" stroke-width="3">
      <path d="M335 126 L335 46 A80 80 0 0 1 404.3 86 Z" fill="#000"/>
      <path d="M335 126 L404.3 86 A80 80 0 0 1 404.3 166 Z" fill="#3b3b3b"/>
      <path d="M335 126 L404.3 166 A80 80 0 0 1 335 206 Z" fill="#4a4a4a"/>
      <path d="M335 126 L335 206 A80 80 0 0 1 265.7 166 Z" fill="#5e5e5e"/>
      <path d="M335 126 L265.7 166 A80 80 0 0 1 265.7 86 Z" fill="#737373"/>
      <path d="M335 126 L265.7 86 A80 80 0 0 1 335 46 Z" fill="#888"/>
    </g>
    <circle cx="335" cy="126" r="37" fill="#555" stroke="#fff" stroke-width="3"/>
    <g fill="#fff" font-size="6" text-anchor="middle">
      <text x="302" y="75">Lorem ipsum</text><text x="302" y="82">dolor sit amet</text>
      <text x="368" y="72">Lorem ipsum</text><text x="368" y="79">dolor sit amet</text>
      <text x="394" y="119">Lorem</text><text x="394" y="126">ipsum dolor</text><text x="394" y="133">sit amet</text>
      <text x="276" y="119">Lorem</text><text x="276" y="126">ipsum dolor</text><text x="276" y="133">sit amet</text>
      <text x="302" y="177">Lorem ipsum</text><text x="302" y="184">dolor sit amet</text>
      <text x="368" y="175">Lorem ipsum</text><text x="368" y="182">dolor sit amet</text>
      <g font-size="9.5"><text x="335" y="115">LOREM</text><text x="335" y="126">IPSUM</text><text x="335" y="137">DOLOR SIT</text><text x="335" y="148">AMET</text></g>
      <text font-size="6.2" letter-spacing=".3"><textPath href="#ring-top" startOffset="50%">LOREM IPSUM DOLOR · LOREM IPSUM DOLOR · LOREM IPSUM DOLOR</textPath></text>
      <text font-size="6.2" letter-spacing=".3"><textPath href="#ring-bottom" startOffset="50%">LOREM IPSUM DOLOR</textPath></text>
    </g>
  </svg>
  <div class="rule" style="left:13px;top:245px;width:428px"></div>
  <div class="footer-text" style="left:378px;top:250px">Lorem ipsum | 04</div>
  <div class="footer-mark" style="left:438px;top:237px"></div>
</section>

<!-- Operations -->
<section class="slide s5">
  <svg class="deco" viewBox="0 0 469 263" aria-hidden="true">
    <circle cx="40" cy="40" r="80" fill="none" stroke="var(--grey-pale)" stroke-width="24"/>
    <rect x="160" y="108" width="110" height="155" fill="var(--grey-pale)"/>
  </svg>
  <div class="heading" style="left:32px;top:93px">Lorem ipsum dolor sit amet.</div>
  <div class="body" style="left:32px;top:109px;width:175px">Lorem ipsum dolor sit amet, consectetur adipiscing elit. Fusce ut diam magna. Cras at orci egestas, tincidunt tortor vitae, viverra mi. Vestibulum in ipsum sapien. Fusce in ipsum id augue ultricies consectetur. Sed et convallis lacus. Nam pretium est eu enim sagittis, quis placerat eros faucibus. Nullam gravida lorem libero, vel sagittis felis interdum non. Duis sit amet commodo libero. Nunc vestibulum facilisis magna sit amet iaculis. Sed viverra, augue sit amet imperdiet lacinia, est sapien sollicitudin neque, ut pellentesque ante sapien vitae nunc. In hac habitasse platea dictumst. Cras porttitor et eros sed dictum.</div>
  <div class="photo" role="img" aria-label="Photo of a refinery silhouette at dusk" style="left:268px;top:0;width:161px;height:263px;background:linear-gradient(180deg,#2e3b45 0%,#5a7079 40%,#b98c6a 65%,#1c1c1e 80%,#111 100%)"></div>
  <div class="rule" style="left:13px;top:245px;width:428px"></div>
  <div class="footer-text" style="left:378px;top:250px;color:#fff">Lorem ipsum | 03</div>
  <div class="footer-mark" style="left:438px;top:237px"></div>
</section>

<!-- Deal highlights -->
<section class="slide s6">
  <svg class="deco" viewBox="0 0 469 263" aria-hidden="true">
    <circle cx="60" cy="20" r="60" fill="none" stroke="var(--grey-pale)" stroke-width="22"/>
    <rect x="0" y="108" width="264" height="155" fill="#f1f1f1"/>
  </svg>
  <div class="heading" style="left:32px;top:26px">Lorem ipsum dolor sit amet,<br>consectetur adipiscing elit.</div>
  <div class="body" style="left:32px;top:61px;width:200px">Lorem ipsum dolor sit amet, consectetur adipiscing elit.</div>
  <div class="bar" style="top:76px;background:var(--grey-mid)">Lorem ipsum dolor</div>
  <div class="bar" style="top:100px;background:var(--grey-dark)">Lorem ipsum dolor</div>
  <div class="bar" style="top:124px;background:var(--grey-mid)">Lorem ipsum dolor</div>
  <div class="bar" style="top:148px;background:var(--grey-dark)">Lorem ipsum dolor</div>
  <div class="bullet" style="top:181px">Lorem ipsum dolor sit amet, consectetur adipiscing elit. Fusce ut diam magna. Cras at orci egestas, tincidunt tortor vitae, viverra mi. Vestibulum in ipsum sapien.</div>
  <div class="bullet" style="top:210px">Lorem ipsum dolor sit amet, consectetur adipiscing elit. Fusce ut diam magna. Cras at orci egestas, tincidunt tortor vitae, viverra mi. Vestibulum in ipsum sapien.</div>
  <div class="photo" role="img" aria-label="Photo of a tall drilling rig against a deep blue sky" style="left:264px;top:0;width:160px;height:263px;background:linear-gradient(180deg,#1d4fa8 0%,#2f66c0 60%,#5a6c86 85%,#6a5a4a 100%)"></div>
  <div class="rule" style="left:13px;top:245px;width:428px"></div>
  <div class="footer-mark" style="left:438px;top:237px"></div>
</section>

</body>
</html>
```